Industrial Automation company requires a business card design

Dravik Automation provides design & build of Automated Equipment for manufacturing industry.
www.dravikautomation-example.com
The equipment we design is used for manufacturing in sectors such as medical device, pharmaceutical, aerospace and electronics.
We require a new business card design which incorporates our (New) logo and the key message words:
Automated Equipment:
Design, Build, Control, Test, Support

Industry/Entity Type

Business

```html
<!DOCTYPE html>
<html lang="en">
<head>
<meta charset="utf-8">
<title>Dravik Automation – Business Card</title>
<link rel="stylesheet" href="https://fonts.googleapis.com/css2?family=Open+Sans:wght@400;600;700&display=swap">
<style>
  :root {
    --backdrop: #e9e7e4;
    --card: #272727;
    --green: #1f8a3e;
    --green-text: #2aa04a;
    --muted: #c9c9c9;
    --icon: #d8d8d8;
  }
  * { margin: 0; padding: 0; box-sizing: border-box; }
  html, body { width: 1200px; height: 900px; overflow: hidden; }
  body {
    background: var(--backdrop);
    font-family: "Open Sans", Arial, sans-serif;
    position: relative;
  }
  .card {
    position: absolute;
    background: var(--card);
    box-shadow: 0 6px 18px rgba(0,0,0,0.25);
    overflow: hidden;
  }
  .card--front { left: 238px; top: 62px; width: 555px; height: 343px; }
  .card--back  { left: 457px; top: 518px; width: 560px; height: 342px; }

  .holder-name {
    position: absolute; left: 47px; top: 29px;
    color: var(--green-text); font-weight: 700; font-size: 18px; letter-spacing: 0.2px;
  }
  .holder-role {
    position: absolute; left: 47px; top: 54px;
    color: var(--muted); font-size: 15px;
  }
  .rule { position: absolute; height: 3px; background: var(--green); }
  .rule--left  { left: 0; top: 146px; width: 134px; }
  .rule--right { left: 419px; top: 188px; width: 136px; }

  .brand {
    position: absolute; display: flex; align-items: center; gap: 12px;
  }
  .brand__dot {
    width: 30px; height: 30px; border-radius: 50%; background: var(--green);
  }
  .brand__name {
    color: var(--green-text); font-weight: 700; text-transform: uppercase; line-height: 1.05;
  }
  .card--front .brand { left: 132px; top: 150px; }
  .card--front .brand__name { font-size: 22px; letter-spacing: 3px; }
  .card--front .brand__name span { display: block; font-size: 15px; letter-spacing: 5.5px; }

  .contacts {
    position: absolute; right: 28px; top: 242px;
    list-style: none; text-align: right;
  }
  .contacts li {
    color: var(--green-text); font-size: 14px; line-height: 20.5px;
    display: flex; justify-content: flex-end; align-items: center; gap: 6px;
  }
  .contacts svg { width: 11px; height: 11px; fill: var(--icon); }

  .band { position: absolute; left: 0; width: 100%; background: var(--green); }
  .band--top { top: 0; height: 10px; }
  .band--bottom { bottom: 0; height: 8px; }
  .card--back .brand { left: 0; right: 0; top: 138px; justify-content: center; }
  .card--back .brand__name { font-size: 38px; letter-spacing: 8px; text-align: center; }
  .card--back .brand__name span { display: block; font-size: 20px; letter-spacing: 9px; margin-top: 4px; }
</style>
</head>
<body>
  <section class="card card--front">
    <p class="holder-name">MARCUS ELWOOD</p>
    <p class="holder-role">Director Operations</p>
    <div class="rule rule--left"></div>
    <div class="brand">
      <div class="brand__dot"></div>
      <p class="brand__name">Dravik<span>Automation</span></p>
    </div>
    <div class="rule rule--right"></div>
    <ul class="contacts">
      <li>+61 400 555 018
        <svg viewBox="0 0 12 12" aria-hidden="true"><rect x="3" y="0.5" width="6" height="11" rx="1.2"/><rect x="4.2" y="2" width="3.6" height="6.5" fill="#272727"/></svg>
      </li>
      <li>marcus@dravik-example.com
        <svg viewBox="0 0 12 12" aria-hidden="true"><rect x="0.5" y="2.5" width="11" height="7.5" rx="0.8"/><path d="M1 3l5 4 5-4" stroke="#272727" stroke-width="1" fill="none"/></svg>
      </li>
      <li>www.dravikautomation-example.com
        <svg viewBox="0 0 12 12" aria-hidden="true"><circle cx="6" cy="6" r="5.5"/><path d="M0.8 6h10.4M6 0.6c-2.4 2.8-2.4 8 0 10.8M6 0.6c2.4 2.8 2.4 8 0 10.8" stroke="#272727" stroke-width="0.8" fill="none"/></svg>
      </li>
    </ul>
  </section>

  <section class="card card--back">
    <div class="band band--top"></div>
    <div class="brand">
      <p class="brand__name">Dravik<span>Automation</span></p>
    </div>
    <div class="band band--bottom"></div>
  </section>
</body>
</html>
```